Lorne Hollow Farm Postcard Design

I am looking for a new postcard design to mail out this season. We are a Farm business that does wholesale and retail and bulk seasoned firewood sales. we sell firewood from anything from bagged wood to tractor trailer loads of wood. We sell firewood in bulk bags. Pick up or delivery available there is no order to big or too small. I need my business name and phone number on the cards Lorne Hollow Farm 848-316-0572 (call or text) I would like it to say we are the best priced guaranteed. I want something that is simple and straight forward but also really catches the eye when they see these in the mail box. I attached my logo and feel free to use photos of split firewood if you would like. id like my email on the card Lornehollowfarm90@mailvista.net.

Target Market(s)

Firewood purchasers

Industry/Entity Type

agriculture

Requirements
Must have
• email phone number logo

```html
<!DOCTYPE html>
<html lang="en">
<head>
<meta charset="utf-8">
<title>Lorne Hollow Farm Postcard</title>
<link href="https://fonts.googleapis.com/css2?family=Mulish:wght@400;600;700&family=Poppins:wght@600;700;800&display=swap" rel="stylesheet">
<style>
:root{
  --page:#bcbdc0;
  --ink:#000;
  --white:#fff;
  --orange:#f26b3a;
  --amber:#f7a93b;
  --gold:#f9c443;
  --line:#b5b5b5;
  --text:#222;
}
*{margin:0;padding:0;box-sizing:border-box}
html,body{width:909px;height:1200px;overflow:hidden;background:var(--page)}
body{position:relative;font-family:"Mulish",sans-serif}
.card{position:absolute;left:93px;width:749px;height:499px;overflow:hidden;background:var(--white)}
.card-front{top:71px}
.card-back{top:612px}
.abs{position:absolute}
.front-bg{position:absolute;inset:0}
.brand-name{position:absolute;left:20px;top:50px;width:122px;font-family:"Poppins",sans-serif;font-weight:700;font-size:17px;line-height:1.15;color:var(--amber);display:flex;align-items:center;gap:7px}
.brand-dot{width:12px;height:12px;border-radius:50%;background:var(--amber);flex:none}
.divider{left:159px;top:23px;width:3px;height:103px;background:#333}
.call-icon{left:190px;top:28px}
.call-label{left:226px;top:22px;font-family:"Poppins",sans-serif;font-weight:700;font-size:12px;color:var(--white)}
.call-number{left:226px;top:36px;font-family:"Poppins",sans-serif;font-weight:700;font-size:21px;color:var(--orange);letter-spacing:.3px}
.intro{left:192px;top:72px;width:215px;font-size:8.2px;line-height:11.1px;color:#e8e8e8}
.headline{left:0;width:455px;top:153px;text-align:center;font-family:"Poppins",sans-serif;font-weight:800;font-size:35px;letter-spacing:-.5px;background:linear-gradient(180deg,var(--gold),var(--orange));-webkit-background-clip:text;background-clip:text;color:transparent}
.subhead{left:0;width:455px;top:207px;text-align:center;font-size:16px;font-weight:600;color:var(--white)}
.truck-glow{left:-10px;top:264px;width:345px;height:345px;border-radius:50%;background:#140b08}
.truck-photo{left:42px;top:256px;width:345px;height:224px;border-radius:8px;background:linear-gradient(135deg,#5a1018,#2a0c0e 60%,#6d6a66)}
.stamp{left:657px;top:14px;width:76px;height:75px;border:1px solid #888}
.addr-line{left:474px;width:253px;height:1px;background:var(--line)}

.badge-bar{left:0;top:0;width:749px;height:57px;background:linear-gradient(180deg,var(--orange),var(--gold))}
.badge{position:absolute;top:13px;display:flex;align-items:center;gap:12px}
.badge-icon{width:29px;height:29px;border-radius:50%;background:linear-gradient(180deg,var(--orange),var(--amber));box-shadow:0 0 0 1.5px rgba(255,255,255,.5);display:flex;align-items:center;justify-content:center}
.badge-text{font-family:"Poppins",sans-serif;font-weight:700;font-size:10.8px;line-height:12.5px;color:var(--white)}
.license{left:552px;top:13px;width:177px;height:29px;border:1.5px solid var(--white);font-family:"Poppins",sans-serif;font-weight:700;font-size:11px;color:var(--white);display:flex;align-items:center;justify-content:center}
.about-title{left:23px;top:75px;font-family:"Poppins",sans-serif;font-weight:700;font-size:13px;color:var(--ink)}
.about-text{left:24px;width:329px;font-size:8.3px;line-height:11.1px;color:var(--text);text-align:justify}
.wood{top:240px;width:82px;height:82px;border-radius:50%}
.wood-hard{left:20px;background:radial-gradient(circle,#c98e5a,#7a4a26)}
.wood-soft{left:147px;background:radial-gradient(circle,#e0b47c,#8a6338)}
.wood-mixed{left:283px;background:radial-gradient(circle,#b7906a,#4a3726)}
.wood-label{top:334px;width:120px;text-align:center;font-family:"Poppins",sans-serif;font-weight:700;font-size:10px;color:var(--ink)}
.site-photo{left:399px;top:57px;width:350px;height:442px;background:linear-gradient(180deg,#8d9096 0%,#5f5a52 45%,#7b756d 100%)}
.back-shapes{position:absolute;left:0;top:0}
.footer-brand{left:20px;top:410px}
.footer-divider{left:163px;top:377px;width:2px;height:107px;background:var(--gold)}
.owner{left:187px;top:386px;font-family:"Poppins",sans-serif;font-weight:700;font-size:14px;color:var(--orange)}
.contact{left:190px;display:flex;align-items:center;gap:10px;font-size:11px;color:var(--white)}
</style>
</head>
<body>

<section class="card card-front">
  <svg class="front-bg" width="749" height="499" viewBox="0 0 749 499">
    <defs>
      <linearGradient id="swoosh" x1="0" y1="0" x2="0" y2="1">
        <stop offset="0" stop-color="#f9b040"/>
        <stop offset="1" stop-color="#f26b3a"/>
      </linearGradient>
    </defs>
    <path d="M0 0 H405 C470 40 500 120 465 250 C435 350 400 420 393 499 H0 Z" fill="url(#swoosh)"/>
    <path d="M0 0 H392 C455 40 478 120 452 250 C425 350 393 420 385 499 H0 Z" fill="#000"/>
  </svg>

  <div class="brand-name"><span class="brand-dot"></span>Lorne Hollow Farm</div>
  <div class="abs divider"></div>

  <svg class="abs call-icon" width="26" height="24" viewBox="0 0 26 24">
    <path d="M3 4 L7 3 L9 8 L7 10 C8 13 10 15 13 16 L15 14 L20 16 L19 20 C11 21 2 12 3 4 Z" fill="#f26b3a"/>
    <rect x="13" y="1" width="12" height="8" rx="4" fill="#f7a93b"/>
    <circle cx="16.5" cy="5" r="1" fill="#000"/><circle cx="19" cy="5" r="1" fill="#000"/><circle cx="21.5" cy="5" r="1" fill="#000"/>
  </svg>
  <div class="abs call-label">CALL OR TEXT</div>
  <div class="abs call-number">848-316-0572</div>
  <p class="abs intro">Lorem ipsum dolor sit amet, consectetur adipiscing elit, sed do eiusmod tempor incididunt ut labore et dolore magna aliqua. Ut enim ad minim veniam, quis nostrud exercitation ullamco laboris nisi ut aliquip ex ea commodo consequat. Duis aute irure dolor in</p>

  <h1 class="abs headline">LORNE HOLLOW FARM</h1>
  <p class="abs subhead">READY FOR PICKUP OR DELIVERY!</p>

  <div class="abs truck-glow"></div>
  <div class="abs truck-photo" role="img" aria-label="Photo of the farm's red tractor truck"></div>

  <div class="abs stamp"></div>
  <div class="abs addr-line" style="top:330px"></div>
  <div class="abs addr-line" style="top:374px"></div>
  <div class="abs addr-line" style="top:416px"></div>
  <div class="abs addr-line" style="top:466px"></div>
</section>

<section class="card card-back">
  <div class="abs site-photo" role="img" aria-label="Photo of a log being moved by a compact loader in a wooded yard"></div>
  <svg class="back-shapes" width="749" height="499" viewBox="0 0 749 499">
    <polygon points="378,57 400,57 420,360 405,360" fill="#f9c443"/>
    <polygon points="0,359 405,359 417,499 0,499" fill="#000"/>
  </svg>

  <div class="abs badge-bar"></div>
  <div class="badge" style="left:17px">
    <div class="badge-icon"><svg width="14" height="14" viewBox="0 0 14 14"><rect x="2" y="1" width="8" height="11" rx="1" fill="#fff"/><circle cx="10.5" cy="10" r="2.5" fill="#fff" stroke="#f26b3a"/></svg></div>
    <div class="badge-text">LICENSED<br>ARBORISTS</div>
  </div>
  <div class="badge" style="left:148px">
    <div class="badge-icon"><svg width="14" height="14" viewBox="0 0 14 14"><circle cx="8" cy="5" r="4" fill="#fff"/><path d="M1 10 H6 L10 11 L13 9 V13 H1 Z" fill="#fff"/></svg></div>
    <div class="badge-text">COMPETITIVE<br>PRICING</div>
  </div>
  <div class="badge" style="left:293px">
    <div class="badge-icon"><svg width="14" height="14" viewBox="0 0 14 14"><rect x="2" y="1" width="8" height="11" rx="1" fill="#fff"/><circle cx="10.5" cy="10" r="3" fill="#fff" stroke="#f26b3a"/></svg></div>
    <div class="badge-text">FREE<br>ESTIMATES</div>
  </div>
  <div class="badge" style="left:417px">
    <div class="badge-icon"><svg width="14" height="14" viewBox="0 0 14 14"><rect x="1" y="6" width="3" height="7" fill="#fff"/><path d="M5 6 L8 1 C10 1 10 3 9 5 H13 V9 L11 13 H5 Z" fill="#fff"/></svg></div>
    <div class="badge-text">HIGH QUALITY<br>PRODUCT</div>
  </div>
  <div class="abs license">LICENSED NO : NJTC482916</div>

  <h2 class="abs about-title">ABOUT US</h2>
  <p class="abs about-text" style="top:104px">Lorem ipsum dolor sit amet, consectetur adipiscing elit, sed do eiusmod tempor incididunt ut labore et dolore magna aliqua. Ut enim ad minim veniam, quis nostrud exercitation ullamco laboris nisi ut aliquip ex ea commodo consequat. Duis aute irure dolor in reprehenderit in voluptate velit esse cillum dolor.</p>
  <p class="abs about-text" style="top:155px">Sed ut perspiciatis unde omnis iste natus error sit voluptatem accusantium doloremque laudantium, totam rem aperiam, eaque ipsa quae ab illo inventore veritatis et quasi architecto beatae vitae dicta sunt explicabo. Nemo enim ipsam voluptatem quia voluptas sit aspernatur aut odit aut fugit, sed quia consequuntur magni dolores eos qui ratione voluptatem sequi nesciunt. Neque porro quisquam est, qui dolorem ipsum quia dolor</p>

  <div class="abs wood wood-hard" role="img" aria-label="Photo of stacked split hardwood"></div>
  <div class="abs wood wood-soft" role="img" aria-label="Photo of stacked softwood log ends"></div>
  <div class="abs wood wood-mixed" role="img" aria-label="Photo of a mixed firewood pile"></div>
  <div class="abs wood-label" style="left:1px">HARDWOOD</div>
  <div class="abs wood-label" style="left:128px">SOFTWOOD</div>
  <div class="abs wood-label" style="left:264px">MIXED</div>

  <div class="brand-name footer-brand" style="top:405px">
    <span class="brand-dot"></span>Lorne Hollow Farm
  </div>
  <div class="abs footer-divider"></div>
  <div class="abs owner">Marcus Elden Vance</div>
  <div class="abs contact" style="top:410px">
    <svg width="12" height="14" viewBox="0 0 12 14"><path d="M6 13 C2 8 1 6 1 5 A5 5 0 0 1 11 5 C11 6 10 8 6 13 Z" fill="#f26b3a"/><circle cx="6" cy="5" r="2" fill="#000"/></svg>
    214 Ridge Mill Rd, Fairhaven NJ 07704
  </div>
  <div class="abs contact" style="top:434px">
    <svg width="12" height="10" viewBox="0 0 12 10"><rect width="12" height="10" fill="#f26b3a"/><path d="M0 0 L6 5 L12 0" stroke="#000" fill="none"/></svg>
    Lornehollowfarm90@mailvista.net
  </div>
  <div class="abs contact" style="top:458px">
    <svg width="13" height="12" viewBox="0 0 26 24"><path d="M3 4 L7 3 L9 8 L7 10 C8 13 10 15 13 16 L15 14 L20 16 L19 20 C11 21 2 12 3 4 Z" fill="#f26b3a"/><rect x="13" y="1" width="12" height="8" rx="4" fill="#f7a93b"/></svg>
    848-316-0572.
  </div>
</section>

</body>
</html>
```